Quorvel Properties - Chat n’ Clink Evening Graphic Invite

We need a graphic design for a corporate reception that we are calling Chat n’ Clink Evening. The invite should read:

"QVR invites you to join us at Chat n’ Clink Evening

Monday, Jan 22nd
6:30 - 8:30 pm EST

Tallow Grill - Lounge Room

48213 E Harrow Glen Rd
Coralmere, KV 33417

Join us for excellent wine and tasty bites at our semi-annual PDA reception. Swing by whenever you can – timing is casual and we'd love to see you there!"

Please feel free to use fun photos from the Tallow Grill gallery: https://www.tallowgrillexample.com/photos

Also, please use the QVR logo attached.

Target Market(s)

Corporate professional

Colors
0054AA
0677BA
7BADD7
CADEEF
E8F1F8

Requirements
Must have
• QVR logo, attached verbiage

```html
<!DOCTYPE html>
<html lang="en">
<head>
<meta charset="utf-8">
<title>Quorvel Properties – Chat n’ Clink Evening</title>
<link rel="stylesheet" href="https://fonts.googleapis.com/css2?family=Figtree:wght@400;500;600;700&display=swap">
<style>
  :root {
    --mat: #b2b2b2;
    --paper: #ffffff;
    --ink: #111111;
    --brand-deep: #1f3d7a;
    --brand-blue: #0677ba;
    --band-blue: #0a70bf;
    --sky: #7badd7;
    --mist: #cadeef;
    --photo-dark: #2c5a82;
  }
  * { margin: 0; padding: 0; box-sizing: border-box; }
  html, body {
    width: 731px; height: 1200px; overflow: hidden;
    background: var(--mat);
    font-family: "Figtree", sans-serif;
    color: var(--ink);
  }
  .invite {
    position: absolute; left: 90px; top: 79px;
    width: 563px; height: 1038px;
    background: var(--paper);
    overflow: hidden;
  }
  .wordmark {
    position: absolute; left: 0; right: 0; top: 68px;
    display: flex; justify-content: center; align-items: center; gap: 12px;
  }
  .wordmark-square {
    width: 30px; height: 30px; background: var(--brand-deep);
  }
  .wordmark-name {
    font-size: 46px; font-weight: 700; color: var(--brand-deep);
    letter-spacing: 1px; line-height: 1;
  }
  .centered { position: absolute; left: 0; right: 0; text-align: center; }
  .lead { top: 201px; font-size: 17px; font-weight: 500; }
  .event-title {
    top: 236px; font-size: 60px; font-weight: 500; line-height: 64px;
    color: var(--brand-blue); letter-spacing: -0.5px;
  }
  .event-date { top: 418px; font-size: 25px; font-weight: 700; }
  .date-rule {
    position: absolute; left: 196px; top: 455px;
    width: 171px; height: 2px; background: var(--brand-blue);
  }
  .event-time { top: 463px; font-size: 18px; font-weight: 500; }
  .venue-band {
    position: absolute; left: 126px; top: 494px;
    width: 311px; height: 29px; background: var(--band-blue);
    color: #fff; font-size: 17px; font-weight: 500;
    display: flex; align-items: center; justify-content: center;
    text-transform: uppercase;
  }
  .venue-address { top: 533px; font-size: 18px; font-weight: 500; line-height: 23px; }
  .welcome-note {
    position: absolute; left: 94px; width: 375px; top: 632px;
    text-align: center; font-size: 12px; font-weight: 500; line-height: 16.5px;
  }
  .venue-photo {
    position: absolute; left: 0; right: 0; top: 720px; bottom: 0;
    background: linear-gradient(180deg, var(--paper) 0%, var(--mist) 18%, var(--sky) 45%, var(--photo-dark) 100%);
  }
</style>
</head>
<body>
  <main class="invite">
    <div class="wordmark">
      <span class="wordmark-square"></span>
      <span class="wordmark-name">QVR</span>
    </div>

    <p class="centered lead">invites you to join us at</p>
    <h1 class="centered event-title">Chat n’ Clink<br>Evening</h1>

    <p class="centered event-date">Monday, Jan 22nd</p>
    <div class="date-rule"></div>
    <p class="centered event-time">6:30 - 8:30 pm EST</p>

    <div class="venue-band">Tallow Grill - Lounge Room</div>
    <p class="centered venue-address">48213 E Harrow Glen Rd<br>Coralmere, KV 33417</p>

    <p class="welcome-note">Join us for excellent wine and tasty bites at our semi-annual PDA reception. Swing by whenever you can – timing is casual and we'd love to see you there!"</p>

    <div class="venue-photo" role="img" aria-label="Blue-toned photo of a long set dining table with chairs, glasses and a floral centerpiece in the restaurant lounge room"></div>
  </main>
</body>
</html>
```